New Orleans history and Study Guide for Professional Tour Guide - City of New Orleans

Book cover. Paperback, 5.25” x 8” book cover, 172 pages, White paper, PageMill template – attached. (PageMill names the template as 180 pages)

This book puts the history of New Orleans into easy sections for persons to learn who are preparing to take the test for the City of New Orleans Certified Visitor Escort Permit. It is required of all tour guides in the city. The attached text for the back cover gives a more complete synopsis of the content.

This Study Guide is a resource for persons seeking a tour guide license. We would like the cover to reflect the professionalism required for test preparation and carry a subtle connection to the creativity of the author as a storyteller and entertainer in the city of New Orleans.

An idea we have had for the front cover would have a background of stylized map of the famed Marigot Ward in the lower half of the cover. Possibly a fan shaped perspective view. The central focus of the Marigot Ward, and the city, is St. Aubin Basilica and Harwell Plaza as seen in these maps and images. https://lnk.example/q7TzWa Maps old and new - https://lnk.example/v3RbYe. A map is not a requirement for cover. Creativity is.

Attached is PageMill/Brindle template, text for front and back cover and two photographs of the author for you to choose from. Both need photoshopping to remove persons behind or next Mr Calloway.

Authors’ previous book: 'Out Along the Levee: Tall Tales of a Storied Port' by Edmund Calloway Link: http://bk.example/7Q2MVXT

Target Market(s)

Persons 18+

Industry/Entity Type

Tourism

Font styles to use
Serif

Requirements
Must have
• Design with book front and back cover with: spine.
• Primary Title is : Study Guide for Professional Tour Guide License Test
• Sub-title: City of New Orleans
Nice to have
• Possible image for design is a Fleur-de-lis, an official emblem of New Orleans. This is a design option and not .a serious Nice To Have.. Some inspiration https://lnk.example/k9DuPx

```html
<!DOCTYPE html>
<html lang="en">
<head>
<meta charset="utf-8">
<title>Study Guide for the Professional Tour Guide Test – Cover</title>
<link href="https://fonts.googleapis.com/css2?family=Raleway:wght@400;500;700;800&family=Arimo:wght@400;700&display=swap" rel="stylesheet">
<style>
  :root {
    --sky-light: #dcf2fb;
    --sky-mid: #a9dcf2;
    --sky-deep: #6fc3e8;
    --skyline-top: #5fa9d6;
    --skyline-mid: #8cc6e6;
    --navy: #1f3a5c;
    --ink: #1d2a36;
    --charcoal: #3a3f45;
    --orange: #f39a1f;
    --orange-deep: #e8870f;
    --white: #ffffff;
  }
  * { box-sizing: border-box; margin: 0; padding: 0; }
  html, body { width: 1200px; height: 932px; overflow: hidden; background: #ffffff; }
  .cover {
    position: relative;
    width: 1200px; height: 932px;
    overflow: hidden;
    background:
      radial-gradient(ellipse at 20% 30%, rgba(255,255,255,.55), transparent 55%),
      radial-gradient(ellipse at 75% 80%, rgba(255,255,255,.5), transparent 50%),
      radial-gradient(ellipse at 60% 35%, rgba(111,195,232,.5), transparent 60%),
      linear-gradient(160deg, var(--sky-mid), var(--sky-light) 45%, var(--sky-mid) 75%, var(--sky-deep));
    font-family: "Arimo", Arial, sans-serif;
    color: var(--ink);
  }

  /* Back cover */
  .back-title {
    position: absolute; left: 0; top: 40px; width: 600px;
    text-align: center;
    font-family: "Raleway", sans-serif; font-weight: 800;
    color: var(--ink); line-height: 1.0;
  }
  .back-title .big { font-size: 24px; display: block; }
  .back-title .small { font-size: 17px; display: block; }
  .back-band {
    position: absolute; left: 57px; top: 129px; width: 521px; height: 22px;
    background: var(--orange);
    color: var(--white); font-size: 14px; text-align: center; line-height: 22px;
  }
  .back-copy {
    position: absolute; left: 64px; top: 186px; width: 488px;
    font-size: 15px; line-height: 24px; color: var(--ink);
    text-align: justify;
  }
  .back-copy p { margin-bottom: 24px; }
  .author-photo {
    position: absolute; left: 66px; top: 582px; width: 116px; height: 123px;
    background: linear-gradient(180deg, #8b8f86 0%, #6b705f 45%, #c9cbc4 100%);
  }
  .author-bio {
    position: absolute; left: 66px; top: 590px; width: 486px;
    font-size: 15px; line-height: 23px; color: var(--ink);
  }
  .author-bio .lead { display: block; padding-left: 140px; text-align: justify; }
  .author-bio em { font-style: italic; text-transform: uppercase; }

  /* Spine */
  .spine {
    position: absolute; left: 578px; top: 0; width: 52px; height: 932px;
  }
  .spine-title, .spine-author {
    position: absolute;
    writing-mode: vertical-rl;
    color: var(--ink);
  }
  .spine-title {
    left: 6px; top: 14px; font-family: "Arimo", sans-serif;
    font-weight: 700; font-size: 14px; line-height: 18px; text-align: center;
  }
  .spine-author {
    top: 496px; left: 14px; font-family: "Raleway", sans-serif; font-size: 20px;
    letter-spacing: 1px; color: var(--charcoal);
  }

  /* Front cover */
  .front { position: absolute; left: 630px; top: 0; width: 570px; height: 932px; }
  .skyline {
    position: absolute; left: 0; top: 0; width: 570px; height: 218px;
    background:
      radial-gradient(ellipse at 60% 40%, rgba(255,255,255,.35), transparent 40%),
      linear-gradient(180deg, var(--skyline-top) 0%, var(--skyline-mid) 40%, rgba(170,215,238,.85) 70%, rgba(217,241,251,0) 100%);
  }
  .photo { position: absolute; }
  .photo-cathedral { left: 3px; top: 224px; width: 233px; height: 286px;
    background: linear-gradient(180deg, #4e5fa8 0%, #8b8fc4 40%, #5a6c4a 75%, #2f3a2a 100%); }
  .photo-statue { left: 243px; top: 224px; width: 173px; height: 129px;
    background: linear-gradient(180deg, #3d8fd8, #9cc8ec); }
  .photo-carriage { left: 243px; top: 360px; width: 173px; height: 150px;
    background: linear-gradient(180deg, #c9b9a4, #8c7a66 60%, #5a4c3e); }
  .photo-crawfish { left: 423px; top: 224px; width: 147px; height: 129px;
    background: linear-gradient(160deg, #e2573a, #c0392b 60%, #f0c2a8); }
  .photo-balcony { left: 423px; top: 360px; width: 147px; height: 150px;
    background: linear-gradient(180deg, #a8c8d8, #6f8a5a 55%, #c9a98a); }

  .front-title {
    position: absolute; left: 0; top: 566px; width: 570px;
    text-align: center; font-family: "Raleway", sans-serif; color: var(--navy);
  }
  .front-title span { display: block; }
  .front-title .line1 { font-size: 48px; font-weight: 800; line-height: 50px; letter-spacing: .5px; }
  .front-title .line2 { font-size: 26px; font-weight: 700; line-height: 34px; letter-spacing: 1px; }
  .front-title .line3 { font-size: 44px; font-weight: 400; line-height: 50px; }
  .front-title .line4 { font-size: 48px; font-weight: 800; line-height: 52px; }
  .front-band {
    position: absolute; left: 0; top: 769px; width: 570px; height: 49px;
    background: linear-gradient(180deg, var(--orange), var(--orange-deep));
    color: var(--white); text-align: center; font-size: 29px; line-height: 49px;
    font-family: "Arimo", sans-serif;
  }
  .front-author {
    position: absolute; left: 0; top: 858px; width: 570px; text-align: center;
    font-family: "Raleway", sans-serif; font-size: 28px; letter-spacing: 2px; color: var(--charcoal);
  }
</style>
</head>
<body>
<div class="cover">

  <section class="back">
    <h2 class="back-title">
      <span class="big">Study Guide</span>
      <span class="small">For The</span>
      <span class="big">Professional Tour</span>
      <span class="big">Guide Test</span>
    </h2>
    <div class="back-band">City Of New Orleans</div>
    <div class="back-copy">
      <p>This STUDY GUIDE is designed to prepare a person for the City of New Orleans Certified Visitor Escort Permit test. Laid out in simple, easy to learn sections this is the basic information needed for passing the city test and moving on to becoming an entertaining tour guide. Your knowledge of the history of New Orleans and Louisiana is key to earning money as a professional tour guide. Tips are directly related to the quality of your stories.</p>
      <p>This guide names the important people, places and events of the city. Recommended readings are based on the author's own personal preferences for reference or pleasure reading.</p>
      <p>A special feature included is a seasoned written Marigot Ward Walking Tour complete with route, stops and full stories. The tour begins at the river and proceeds through a section of the Ward favored among tour guides. It is the bread and butter of Marigot Ward tours.</p>
    </div>
    <div class="author-photo" role="img" aria-label="Portrait photograph of the author in a sun hat"></div>
    <p class="author-bio">
      <span class="lead">Ed Calloway worked as a tour guide in the City for years. He taught the Professional Tourguiding class at Bayou Crescent Community College, plus a class in Research and Storytelling. He is an avid reader of local history. He earned a Ph.D. from Pacific Coast University in Communication, plus BA</span>
      and MA degrees from Gulf State University in Public Speaking.<br>
      A companion to this STUDY GUIDE is Dr. Calloway's <em>Out Along the Levee</em> – Tall Tales of a Storied Port.
    </p>
  </section>

  <section class="spine">
    <div class="spine-title">STUDY GUIDE FOR THE<br>PROFESSIONAL TOURGUIDE TEST</div>
    <div class="spine-author">EDMUND C CALLOWAY JR., PHD</div>
  </section>

  <section class="front">
    <div class="skyline" role="img" aria-label="Faded blue city skyline photograph with a faint city emblem"></div>
    <div class="photo photo-cathedral" role="img" aria-label="Basilica at dusk with a lit plaza and carriages"></div>
    <div class="photo photo-statue" role="img" aria-label="Equestrian statue against a blue sky"></div>
    <div class="photo photo-crawfish" role="img" aria-label="Boiled crawfish close-up"></div>
    <div class="photo photo-carriage" role="img" aria-label="Mule-drawn carriage on a street"></div>
    <div class="photo photo-balcony" role="img" aria-label="Iron balcony building with hanging plants"></div>

    <h1 class="front-title">
      <span class="line1">STUDY GUIDE</span>
      <span class="line2">FOR THE</span>
      <span class="line3">PROFESSIONAL TOUR</span>
      <span class="line4">GUIDE TEST</span>
    </h1>
    <div class="front-band">City Of New Orleans</div>
    <div class="front-author">EDMUND C CALLOWAY JR., PHD</div>
  </section>

</div>
</body>
</html>
```